Vandrel Group — Business Card Design Brief
Overview
Design a double-sided business card for Vandrel Group that highlights our two service arms: Vandrel Communications (telecommunications) and Vandrel Energy (business energy solutions). The card should feel smart and stand out when handed to clients.

Objectives
Showcase our areas of specialty clearly.
Reflect the overall Vandrel / Vandrel Group brand while acknowledging both arms.
Explore using both logos (Communications + Energy) or one unified logo, depending on the design.

Deliverables
One double-sided business card design (front + back).

Content & Copy
Front (preferred): Logo: Vandrel / Vandrel Group
Descriptor: Business Communications | Business Energy
Back:My contact details and company details
Core products: Business Mobile • Telephony • Internet • Business Energy Solutions

Brand & Visual Direction
We have a group logo currently tailored more toward telecoms, plus a separate Vandrel Energy logo.
Please explore layouts that use both logos or just one, whichever works best.
Color: I wouldn't mind seeing an option using our the Blue/Purple gradient from our website (vandrel-example.co.uk), but also open to non-gradient approaches and other colours..

Overall look: Smart, modern, and distinctive.
Format & Print Specs
Double-sided business card format. (Use a standard size

Must-Haves
Front: Vandrel wording or Vandrel Group wording with atleast 1 logo also on front “Business Communications | Business Energy.”

Back: Contact + company details and core products.
A design that stands out while remaining professional.

Nice-to-Have Options
A gradient version using our site’s Blue/Purple gradient.
A non-gradient version.
A dual-logo treatment versus a single-logo treatment.

Thanks
Dominic

```html
<!DOCTYPE html>
<html lang="en">
<head>
<meta charset="utf-8">
<title>Vandrel Group — Business Card</title>
<link rel="stylesheet" href="https://fonts.googleapis.com/css2?family=Lato:wght@400;700;900&display=swap">
<style>
  :root {
    --stage: #8f8f8f;
    --paper: #ffffff;
    --navy: #1d1a6a;
    --ink: #26235f;
    --violet: #9a1ccc;
    --rule: #1f63d1;
    --brand-blue: #1e6fe0;
    --grad-violet: #8b0fc0;
    --grad-navy: #1e1a6c;
    --grad-blue: #1f55b8;
    --white: #ffffff;
  }
  * { margin: 0; padding: 0; box-sizing: border-box; }
  html, body {
    width: 1200px; height: 2297px; overflow: hidden;
    background: var(--stage);
    font-family: "Lato", Arial, sans-serif;
  }
  .card {
    position: absolute; left: 286px; width: 628px; height: 359px;
    border-radius: 22px; overflow: hidden;
  }

  /* Back: contact side */
  .card-back { top: 1324px; background: var(--paper); color: var(--ink); }
  .brand-lockup {
    position: absolute; right: 42px; top: 96px;
    display: flex; align-items: center; gap: 12px;
  }
  .brand-dot { width: 30px; height: 30px; border-radius: 50%; background: var(--brand-blue); }
  .brand-name { font-weight: 900; font-size: 44px; color: var(--navy); letter-spacing: 0.5px; line-height: 1; }
  .holder { position: absolute; left: 32px; top: 136px; }
  .holder-name { font-weight: 900; font-size: 28px; color: var(--navy); line-height: 1; }
  .holder-role { font-size: 15px; color: var(--violet); margin-top: 4px; }
  .rule { position: absolute; left: 32px; right: 38px; height: 1.5px; background: var(--rule); }
  .rule-top { top: 196px; }
  .rule-bottom { top: 304px; }
  .contacts { position: absolute; left: 34px; top: 210px; list-style: none; font-size: 14px; }
  .contacts li { display: flex; align-items: center; height: 20.5px; }
  .contacts svg { width: 11px; height: 11px; margin-right: 12px; fill: var(--violet); }
  .address { position: absolute; right: 42px; top: 210px; text-align: right; font-size: 14px; line-height: 20.5px; }
  .address-company { color: var(--violet); font-weight: 700; }
  .services {
    position: absolute; left: 32px; right: 38px; top: 318px;
    display: flex; justify-content: space-between;
    font-size: 12.5px; letter-spacing: 1.1px; color: var(--ink);
  }

  /* Front: brand side */
  .card-front {
    top: 1751px;
    background:
      radial-gradient(circle at 0% 0%, var(--grad-violet) 0%, rgba(139,15,192,0) 38%),
      linear-gradient(135deg, var(--grad-navy) 45%, var(--grad-blue) 100%);
    color: var(--white); text-align: center;
  }
  .front-dot {
    position: absolute; left: 50%; top: 62px; transform: translateX(-50%);
    width: 120px; height: 120px; border-radius: 50%; background: var(--brand-blue);
  }
  .front-name {
    position: absolute; left: 0; right: 0; top: 204px;
    font-weight: 900; font-size: 72px; line-height: 1; letter-spacing: 1px;
  }
  .front-tagline {
    position: absolute; left: 0; right: 0; top: 320px;
    font-size: 13px; font-weight: 700; letter-spacing: 4.5px;
  }
</style>
</head>
<body>
  <section class="card card-back">
    <div class="brand-lockup">
      <span class="brand-dot"></span>
      <span class="brand-name">VANDREL</span>
    </div>
    <div class="holder">
      <h1 class="holder-name">DOMINIC HARTWELL</h1>
      <p class="holder-role">Managing Director</p>
    </div>
    <div class="rule rule-top"></div>
    <ul class="contacts">
      <li><svg viewBox="0 0 12 12"><path d="M3 0h6a1 1 0 0 1 1 1v10a1 1 0 0 1-1 1H3a1 1 0 0 1-1-1V1a1 1 0 0 1 1-1zm0 2v7h6V2z"/></svg>+44 7700 900 318</li>
      <li><svg viewBox="0 0 12 12"><path d="M2.5 0.5l2 2.5-1 1.5c.8 1.7 2.2 3.1 4 4l1.5-1 2.5 2-1.2 2c-5 0-9.3-4.3-9.3-9.3z"/></svg>+44 (0) 161 496 0274</li>
      <li><svg viewBox="0 0 12 12"><path d="M0 2h12v1L6 7 0 3zm0 2.5l6 4 6-4V10H0z"/></svg>dominic.hartwell@vandrel-example.co.uk</li>
      <li><svg viewBox="0 0 12 12"><path d="M6 0a6 6 0 1 0 0 12A6 6 0 0 0 6 0zm0 1.5a4.5 4.5 0 1 1 0 9 4.5 4.5 0 0 1 0-9zM4 3l2.5 1.5L5 7 3.5 5z"/></svg>www.vandrel-example.co.uk</li>
    </ul>
    <address class="address" style="font-style:normal">
      <div class="address-company">Vandrel Group</div>
      <div>24 Calder Row</div>
      <div>Manchester</div>
      <div>M2 7QX</div>
    </address>
    <div class="rule rule-bottom"></div>
    <div class="services">
      <span>BUSINESS MOBILE</span><span>|</span><span>TELEPHONY</span><span>|</span><span>INTERNET</span><span>|</span><span>SECURITY</span><span>|</span><span>ENERGY SOLUTIONS</span>
    </div>
  </section>

  <section class="card card-front">
    <span class="front-dot"></span>
    <h2 class="front-name">VANDREL</h2>
    <p class="front-tagline">COMMUNICATIONS &nbsp;|&nbsp; ENERGY</p>
  </section>
</body>
</html>
```